Brochure & Business card design

Looking for a new business card design i want it to be modern and sharp looking i usually order plastic business cards, and i would like to make the colors like the logo teal/charcoal i will like to have our services on icons with words.... our services are
ROOFING GUTTERS PAINTING PRESSURE WASHING EXTERIOR DESIGN & ATTIC VENTILATION. I also want to add my credentials

Target Market(s)

Oregon local market

Industry/Entity Type

Residential Construction

Contact Information for Business Card

Business info, services, number, website

Font styles to use
Serif
Sans Serif

Colors
33b8a4
5c5c5c
ffffff

Requirements
Must have
• Dale Finch
• Cell:
• Office:
• Email:
• Website:
• also i need our social media icons
• Services ROOFING GUTTERS PAINTING PRESSURE WASHING EXTERIOR DESIGN & ATTIC VENTILATION
• -icons for number, web, email, cell
• OR #584312
• Wa #KTRABLD461X7
Nice to have
• -Clean design Front & Back
• -Icons
• -shape House just like logo design
• -First Impression
Should not have
• Not Busy or lost of eye contact

```html
<!DOCTYPE html>
<html lang="en">
<head>
<meta charset="utf-8">
<title>Cedarline Home Exteriors – Business Card</title>
<link href="https://fonts.googleapis.com/css2?family=Roboto:wght@400;500;700&family=Roboto+Condensed:wght@700&display=swap" rel="stylesheet">
<style>
  :root {
    --teal: #1a9384;
    --teal-bright: #33b8a4;
    --charcoal: #5c5c5c;
    --white: #ffffff;
    --backdrop: #c9c9c9;
    --badge-dark: #111111;
    --badge-light: #e9e9e9;
  }
  * { margin: 0; padding: 0; box-sizing: border-box; }
  html, body { width: 1200px; height: 1200px; overflow: hidden; }
  body { background: var(--backdrop); font-family: "Roboto", sans-serif; position: relative; }

  .card { position: absolute; width: 800px; height: 457px; left: 218px; }

  /* Front */
  .card-front { top: 115px; background: var(--teal); color: var(--white); }
  .license { position: absolute; top: 30px; font-size: 19px; font-weight: 500; }
  .license-wa { left: 41px; }
  .license-or { right: 42px; }
  .front-brand {
    position: absolute; top: 150px; left: 0; right: 0;
    display: flex; justify-content: center; align-items: center; gap: 16px;
    font-size: 52px; font-weight: 700; letter-spacing: 3px;
  }
  .brand-square { width: 34px; height: 34px; background: var(--white); }
  .services {
    position: absolute; top: 377px; left: 160px; width: 500px;
    text-align: center; font-size: 19.5px; line-height: 24px; letter-spacing: 0.2px;
  }
  .sep { display: inline-block; width: 9px; height: 9px; background: var(--white); margin: 0 4px 3px; vertical-align: middle; }
  .badge-cert { position: absolute; left: 23px; top: 375px; width: 126px; height: 47px; background: var(--badge-light); border-bottom: 4px solid #d8332b; }
  .badge-accredited { position: absolute; left: 664px; top: 380px; width: 111px; height: 42px; background: var(--badge-dark); border-radius: 5px; border-left: 38px solid var(--badge-light); }

  /* Back */
  .card-back { top: 638px; background: var(--white); }
  .back-brand {
    position: absolute; left: 137px; top: 150px; width: 230px;
    color: var(--teal); font-weight: 700; font-size: 30px; line-height: 36px; text-align: center;
  }
  .back-brand .brand-square { background: var(--teal); width: 28px; height: 28px; margin: 0 auto 12px; }
  .divider { position: absolute; left: 395px; top: 130px; width: 3px; height: 195px; background: var(--charcoal); opacity: 0.7; }
  .contact { position: absolute; left: 425px; top: 122px; color: var(--charcoal); }
  .contact-name { font-family: "Roboto Condensed", sans-serif; font-size: 32px; color: var(--teal); letter-spacing: 0.5px; line-height: 36px; }
  .contact-title { font-size: 20px; font-weight: 500; line-height: 24px; }
  .contact-address { margin-top: 15px; font-size: 19.5px; line-height: 24px; }
  .contact-list { list-style: none; margin-top: 12px; font-size: 19.5px; line-height: 25.5px; }
  .contact-list li { display: flex; align-items: center; gap: 12px; }
  .contact-list svg { width: 18px; height: 18px; fill: var(--teal); }
  .back-rule { position: absolute; left: 0; right: 0; top: 418px; height: 3px; background: #b8b8b8; }
  .back-band { position: absolute; left: 0; right: 0; bottom: 0; height: 33px; background: var(--teal); }
</style>
</head>
<body>
  <section class="card card-front">
    <p class="license license-wa">Wa #KTRABLD461X7</p>
    <p class="license license-or">OR #584312</p>
    <div class="front-brand"><span class="brand-square"></span>CEDARLINE</div>
    <div class="badge-cert" role="img" aria-label="Roofing contractor certification badge"></div>
    <p class="services">ROOFING <span class="sep"></span>GUTTERS <span class="sep"></span>PAINTING <span class="sep"></span>PRESSURE WASHING&nbsp; EXTERIOR DESIGN &amp; ATTIC VENTILATION</p>
    <div class="badge-accredited" role="img" aria-label="Accredited business badge"></div>
  </section>

  <section class="card card-back">
    <div class="back-brand"><div class="brand-square"></div>CEDARLINE<br>HOME EXTERIORS</div>
    <div class="divider"></div>
    <div class="contact">
      <h1 class="contact-name">DALE FINCH</h1>
      <p class="contact-title">CEO/FOUNDER</p>
      <p class="contact-address">1420 Cedar Hollow Road<br>Salem, Oregon 97301</p>
      <ul class="contact-list">
        <li><svg viewBox="0 0 18 18" aria-hidden="true"><path d="M5 0h8a1.5 1.5 0 0 1 1.5 1.5v15A1.5 1.5 0 0 1 13 18H5a1.5 1.5 0 0 1-1.5-1.5v-15A1.5 1.5 0 0 1 5 0zm0 2v12h8V2zm4 13a1 1 0 1 0 0 2 1 1 0 0 0 0-2z"/></svg>503-555-0148</li>
        <li><svg viewBox="0 0 18 18" aria-hidden="true"><path d="M1 4h16v10H1zm1.5 1.2v.4L9 10l6.5-4.4v-.4zM2.5 7.4v5.3h13V7.4L9 11.8z"/></svg>hello@cedarlinehomes.com</li>
        <li><svg viewBox="0 0 18 18" aria-hidden="true"><circle cx="9" cy="9" r="8"/><path d="M5 5c2 0 3 1 2.5 2.5S9 9 8 11s-2 1-2 3M11 3c0 2 2 2 3 3M12 11c1 0 2 1 1.5 3" stroke="#fff" stroke-width="1.4" fill="none"/></svg>CedarlineHomes.com</li>
      </ul>
    </div>
    <div class="back-rule"></div>
    <div class="back-band"></div>
  </section>
</body>
</html>
```